Swimming Pool Service business card needed!!!! Please

Hi Everyone! Thanks for looking at my contest. I PROMISE to provide excellent feedback during this process.

I am starting a new swimming pool cleaning business in San Diego, California and would like your help in making a business card for me.

I like easy to read, classy and sophisticated.

I am having a website designed and I'm looking for it to have pictures of really clean & clear pools.

I really like the blue on white color format, but open to other colors.

I do not have a logo, but the name of my company is GLIMMERTIDE POOL SERVICE.

My tag line is: Pools so clean, you can see yourself "in" them. (does not need to have the quotes around "in"...maybe just italics for this word IN?) You decide for me.

I would like to have a logo designed that incorporates some sort of easy to read letters. I do not want cursive (handwriting) letters. I thought about having a "reflection" of letters (mirror image), but think that this will be hard to read from far away. Maybe you can surprise me and come up with an idea that works using the a mirror image....but I'm not sure. I was leaning toward plain old BLOCK letters as I think it would be easy to read on my truck.

I would like to have the NAQTR and WBK logos on the back of the card. I have attached those two as files. You can put other things on the back as well, but I need these two logos on there. Or maybe put them on the front of the card if you have a better idea for the back of the card! :-)

Maybe blue on the back of the card and white on the front of the card? I don't know, I'm just thinking out loud.

I had another card done awhile ago called HARBORLINE TEES. I have uploaded a copy of that card for your reference. I don't want this card to be the same as my new company is a swimming pool cleaning company, but I wanted you to see what I liked in the past.

THANK YOU!!!!
Updates

Reason: Partner out of town and want their feedback....so need more time to decide and designs still coming in.

Industry/Entity Type

Business

Contact Information for Business Card

GLIMMERTIDE POOL SERVICE
Dale Wexby
Owner
4817 Quarry Bend Ave. #512
San Diego, CA 92417
858-291-6083
www.glimmertidepoolservice.example

Font styles to use
Sans Serif

Colors
0255a3
3176b5
ffffff

Requirements
Nice to have
• Some things to (possibly) add to back of card (in no particular order)
• WBK logo
• NAQTR logo
• Free Estimates
• Residential and Commercial Services
• Equipment Repairs
• Saltwater Systems
• Licensed, Bonded, Insured
• Family Owned and Operated
• No Contracts
• =======================
• Check out the FolioMint business card that i attached.
• i think they did this using a chrome overlay.
• Can any of you guys design that? or is that done at my printer?
• ==================
Should not have
• Hi Designers-
• The first round of cards came back and let's stay away from the light blue (powder blue) color. I don't like the look of it on the business cards.
• Also, the pool company JPG's that I attached are other logos of pool companies that I liked. I don't want them to be on my card. The only logos that should be on my card are the one you are going to come up with for my company, the WBK logo and the NAQTR logo.
• Lastly, no vertical cards and no split cards (logo on left, contact info on right side).
• Thanks much!

```html
<!DOCTYPE html>
<html lang="en">
<head>
<meta charset="utf-8">
<title>Glimmertide Pool Service – Business Card</title>
<link rel="stylesheet" href="https://fonts.googleapis.com/css2?family=Bebas+Neue&display=swap">
<style>
  :root {
    --stage-grey: #b7b8ba;
    --card-white: #ffffff;
    --brand-blue: #0255a3;
    --deep-blue: #175ba8;
    --mid-blue: #6f86c4;
    --echo-blue: #2a78bb;
    --ink: #111111;
  }
  html, body {
    margin: 0;
    padding: 0;
    width: 963px;
    height: 1200px;
    overflow: hidden;
    background: var(--stage-grey);
  }
  .sheet {
    display: block;
    width: 963px;
    height: 1200px;
  }
  .card-type {
    font-family: "Bebas Neue", "Oswald", sans-serif;
  }
  .brand-name { fill: var(--card-white); font-size: 90px; }
  .brand-echo { fill: var(--echo-blue); font-size: 86px; }
  .tagline { fill: var(--card-white); font-size: 36px; letter-spacing: 2px; }
  .owner-name { fill: var(--brand-blue); font-size: 96px; letter-spacing: 8px; }
  .owner-title { fill: var(--ink); font-size: 44px; letter-spacing: 3px; }
  .contact-line { fill: var(--ink); font-size: 38px; letter-spacing: 3px; }
</style>
</head>
<body>
<svg class="sheet" viewBox="0 0 963 1200" xmlns="http://www.w3.org/2000/svg">
  <defs>
    <linearGradient id="front-fade" x1="0" y1="0" x2="0" y2="1">
      <stop offset="0" stop-color="#175ba8"/>
      <stop offset="0.45" stop-color="#6f86c4"/>
      <stop offset="1" stop-color="#ffffff"/>
    </linearGradient>
    <linearGradient id="back-frame" x1="0" y1="0" x2="0" y2="1">
      <stop offset="0" stop-color="#175ba8"/>
      <stop offset="0.5" stop-color="#6f86c4"/>
      <stop offset="1" stop-color="#ffffff"/>
    </linearGradient>
    <radialGradient id="cert-badge-fill" cx="0.5" cy="0.4" r="0.6">
      <stop offset="0" stop-color="#e4e6f4"/>
      <stop offset="0.6" stop-color="#7c84c6"/>
      <stop offset="1" stop-color="#3646a0"/>
    </radialGradient>
  </defs>

  <!-- Front of card -->
  <g class="card card-front">
    <rect x="71" y="65" width="821" height="481" fill="var(--card-white)"/>
    <rect x="86" y="81" width="790" height="450" fill="url(#front-fade)"/>
    <text class="card-type brand-name" x="130" y="295" textLength="701" lengthAdjust="spacingAndGlyphs">GLIMMERTIDE POOL SERVICE</text>
    <g class="brand-echo-group" transform="translate(0 300)">
      <g transform="matrix(1 0 0.5 -1 0 0)">
        <text class="card-type brand-echo" x="131" y="0" textLength="690" lengthAdjust="spacingAndGlyphs" aria-hidden="true">GLIMMERTIDE POOL SERVICE</text>
      </g>
    </g>
    <text class="card-type tagline" x="130" y="394" textLength="701" lengthAdjust="spacingAndGlyphs">POOLS SO CLEAN, YOU CAN SEE YOURSELF IN THEM.</text>
  </g>

  <!-- Back of card -->
  <g class="card card-back">
    <rect x="71" y="650" width="821" height="482" fill="var(--card-white)"/>
    <rect x="81" y="661" width="800" height="459" fill="url(#back-frame)"/>
    <rect x="90" y="670" width="782" height="450" fill="var(--card-white)"/>

    <text class="card-type owner-name" x="100" y="754" textLength="326" lengthAdjust="spacingAndGlyphs">DALE WEXBY</text>
    <text class="card-type owner-title" x="102" y="791" textLength="112" lengthAdjust="spacingAndGlyphs">OWNER</text>

    <text class="card-type contact-line" x="102" y="1019" textLength="422" lengthAdjust="spacingAndGlyphs">4817 QUARRY BEND AVE. #512</text>
    <text class="card-type contact-line" x="102" y="1048" textLength="273" lengthAdjust="spacingAndGlyphs">SAN DIEGO, CA 92417</text>
    <text class="card-type contact-line" x="102" y="1078" textLength="188" lengthAdjust="spacingAndGlyphs">858-291-6083</text>
    <text class="card-type contact-line" x="102" y="1108" textLength="472" lengthAdjust="spacingAndGlyphs">WWW.GLIMMERTIDEPOOLSERVICE.EXAMPLE</text>

    <circle class="cert-badge" cx="770" cy="786" r="96" fill="url(#cert-badge-fill)" stroke="var(--ink)" stroke-width="3" role="img" aria-label="WBK certification badge"/>
    <g class="member-badge" role="img" aria-label="NAQTR membership badge">
      <circle cx="770" cy="1012" r="93" fill="var(--card-white)" stroke="var(--ink)" stroke-width="5"/>
      <circle cx="770" cy="1012" r="78" fill="var(--ink)"/>
    </g>
  </g>
</svg>
</body>
</html>
```